upgrade joomla to HTML5 on existing website

This project will need designer to improve/upgrade existing website that was designed from joomla (CMS) to HTML5. The current website code would not given and designer only can visit the site to take all info to migrate it to new design.
Some addition of new image, info and web action will be added here. The designer must provide all source code and step to modify the newly design web for future modification. The existing web site is www.velmorquistline.com.
Requirements
Must have
- knowledge on:-
- HTML5
- Twitter dock configuration
- web mail configuration
- CMS

```html
<!DOCTYPE html>
<html lang="en">
<head>
<meta charset="utf-8">
<title>Velmorquistline — Web Application for Cellular Network</title>
<link href="https://fonts.googleapis.com/css2?family=Noto+Sans:wght@400;700&display=swap" rel="stylesheet">
<style>
  :root{
    --brand:#2b6a9a;
    --brand-dark:#245a84;
    --heading:#1f6fa3;
    --text:#555;
    --muted:#666;
    --panel:#f1f1f1;
    --white:#fff;
    --line:#d8d8d8;
  }
  *{box-sizing:border-box;margin:0;padding:0}
  html,body{width:1200px;height:1054px;overflow:hidden}
  body{font-family:"Noto Sans",Verdana,sans-serif;background:var(--white);color:var(--text);position:relative}
  .wrap{position:absolute;left:160px;width:884px}

  /* header */
  .site-header{position:absolute;top:0;left:0;width:1200px;height:118px}
  .brand{position:absolute;left:165px;top:26px;display:flex;align-items:center;gap:12px}
  .brand-mark{width:54px;height:54px;border-radius:50%;background:var(--brand)}
  .brand-tagline{font-size:6px;font-weight:700;color:#555;letter-spacing:.2px}
  .brand-name{font-size:18px;font-weight:700;color:#3b3bd6;margin-top:2px}
  .account{position:absolute;right:157px;top:24px;font-size:13px;color:#666}
  .social{position:absolute;right:157px;top:58px;display:flex;gap:3px}
  .social span{width:19px;height:19px;border-radius:2px;background:#8a9bb0}

  /* nav */
  .main-nav{position:absolute;top:118px;left:0;width:1200px;height:42px;background:var(--brand);border-bottom:1px solid #6f9fc4}
  .main-nav ul{list-style:none;display:flex;position:absolute;left:160px;height:41px}
  .main-nav li{color:var(--white);font-size:13px;line-height:41px;padding:0 25px 0 20px;border-right:1px solid var(--brand-dark)}

  /* hero */
  .hero{position:absolute;top:160px;left:0;width:1200px;height:310px;background:linear-gradient(#a8a8a8,#8f8f8f 60%,#a8a8a8)}
  .hero-visual{position:absolute;left:160px;top:0;width:884px;height:310px;
    background:radial-gradient(ellipse at 55% 35%,#d6f6ff 0%,#3fa8b8 18%,#11505e 48%,#062a33 85%)}
  .hero-quote{position:absolute;left:27px;top:17px;width:700px;color:var(--white);font-size:14.5px;line-height:17px}
  .hero-arrow{position:absolute;top:143px}
  .hero-arrow.prev{left:27px}.hero-arrow.next{right:28px}

  /* intro */
  .intro{top:498px;height:140px}
  .section-title{font-size:16px;font-weight:400;color:var(--heading);letter-spacing:.3px;text-transform:uppercase}
  .welcome{position:absolute;left:0;width:570px}
  .welcome .section-title{margin-left:7px}
  .welcome p{width:550px;font-size:12px;line-height:14px;margin-top:12px;margin-left:5px;color:var(--muted)}
  .btn{display:inline-block;font-size:12px;color:#555;background:linear-gradient(#fafafa,#e8e8e8);border:1px solid #dcdcdc;border-radius:4px;padding:0 22px;line-height:32px}
  .welcome .btn{position:absolute;right:-12px;top:100px}
  .divider{position:absolute;left:594px;top:0;width:1px;height:140px;background:var(--line)}
  .news{position:absolute;left:614px;width:270px}
  .news-head{display:flex;align-items:center;gap:11px;margin-top:-2px}
  .icon-circle{width:29px;height:29px;border-radius:50%;background:#2e86bb;display:flex;align-items:center;justify-content:center;flex:none}
  .news-item{display:flex;gap:4px;margin-top:6px}
  .news-thumb{width:130px;height:96px;background:linear-gradient(135deg,#f4f4f4,#cfe3f2 45%,#f6dfa0 70%,#f4f4f4)}
  .news-text{font-size:12px;color:#444;line-height:14px}
  .news-text h3{font-size:12px;font-weight:400;color:var(--heading);margin-bottom:12px}
  .news-text p+p{margin-top:12px}

  /* feature cards */
  .features{top:667px;height:325px;display:flex;gap:9px}
  .card{position:relative;width:289px;height:325px;background:var(--panel);padding:10px 14px 0 14px}
  .card-head{display:flex;align-items:center;gap:9px;margin-left:6px}
  .card-media{height:148px;margin-top:8px}
  .media-people{background:linear-gradient(135deg,#eef4f9,#cfe2ef 50%,#eef4f9)}
  .media-org{background:linear-gradient(160deg,#fafafa 40%,#5e9fd8 70%,#2d6fb0)}
  .media-values{background:linear-gradient(180deg,#ffffff,#fdf0d6 50%,#ffffff)}
  .card p{font-size:12px;line-height:13.8px;color:var(--muted);margin-top:6px;padding:0 2px 0 7px}
  .card .btn{position:absolute;right:10px;bottom:8px}

  /* footer */
  .site-footer{position:absolute;top:1012px;left:0;width:1200px;height:42px;background:var(--brand);color:var(--white);font-size:10px;text-align:center;line-height:42px;letter-spacing:.2px}
</style>
</head>
<body>
  <header class="site-header">
    <div class="brand">
      <div class="brand-mark"></div>
      <div>
        <div class="brand-tagline">WEB APPLICATION FOR CELLULAR NETWORK</div>
        <div class="brand-name">Velmorquistline</div>
      </div>
    </div>
    <div class="account">Login | Register</div>
    <div class="social"><span></span><span></span><span></span><span></span></div>
  </header>

  <nav class="main-nav">
    <ul>
      <li>Home</li><li>About Us</li><li>Services</li><li>Products</li><li>News &amp; Updates</li><li>Contact Us</li><li>Webmail</li>
    </ul>
  </nav>

  <section class="hero">
    <div class="hero-visual" role="img" aria-label="Digital data corridor lined with computer monitors glowing in teal light">
      <p class="hero-quote">The world is very different now. For man holds in his mortal hands the power to abolish all forms of human poverty, and all forms of human life.</p>
      <svg class="hero-arrow prev" width="29" height="29" viewBox="0 0 29 29"><circle cx="14.5" cy="14.5" r="13" fill="none" stroke="#fff" stroke-width="2"/><path d="M17 8 L9 14.5 L17 21 L14.5 14.5Z" fill="#fff"/></svg>
      <svg class="hero-arrow next" width="29" height="29" viewBox="0 0 29 29"><circle cx="14.5" cy="14.5" r="13" fill="none" stroke="#fff" stroke-width="2"/><path d="M12 8 L20 14.5 L12 21 L14.5 14.5Z" fill="#fff"/></svg>
    </div>
  </section>

  <section class="wrap intro">
    <div class="welcome">
      <h2 class="section-title">Welcome to Velmorquistline</h2>
      <p>Velmorquistline Sdn. Bhd. is a very fast growing company who provides the missing links between management and engineering team and also between Headquarter and regional team with advance architecture system. With these solutions, it will minimize the needs of data redundancy due to centralize database system and can be accessed by many departments.</p>
      <span class="btn">Read More</span>
    </div>
    <div class="divider"></div>
    <div class="news">
      <div class="news-head">
        <span class="icon-circle"><svg width="13" height="15" viewBox="0 0 13 15"><rect x="1" y="1" width="11" height="13" rx="1" fill="#fff"/><path d="M3 5h7M3 7.5h7M3 10h7" stroke="#2e86bb" stroke-width="1"/></svg></span>
        <h2 class="section-title">News &amp; Updates</h2>
      </div>
      <div class="news-item">
        <div class="news-thumb" role="img" aria-label="Colourful pie and bar chart under a magnifying glass"></div>
        <div class="news-text">
          <h3>CELL ANALYSIS</h3>
          <p>Cell analysis</p>
          <p>Cell Analysis provides fast access to...</p>
        </div>
      </div>
    </div>
  </section>

  <section class="wrap features">
    <article class="card">
      <div class="card-head">
        <span class="icon-circle"><svg width="14" height="14" viewBox="0 0 14 14"><circle cx="7" cy="4" r="3" fill="#fff"/><path d="M1 14 C1 8 13 8 13 14Z" fill="#fff"/></svg></span>
        <h2 class="section-title">About Velmorquistline</h2>
      </div>
      <div class="card-media media-people" role="img" aria-label="Network of connected blue figures"></div>
      <p>Velmorquistline Sdn. Bhd. is a very fast growing company who provides the missing links between management and engineering team and also between Headquarter and regional team with advance architecture system.</p>
      <span class="btn">Read More</span>
    </article>
    <article class="card">
      <div class="card-head">
        <span class="icon-circle"><svg width="13" height="15" viewBox="0 0 13 15"><rect x="1" y="1" width="11" height="13" rx="1" fill="#fff"/><path d="M3 5h7M3 7.5h7M3 10h7" stroke="#2e86bb" stroke-width="1"/></svg></span>
        <h2 class="section-title">Our Organization</h2>
      </div>
      <div class="card-media media-org" role="img" aria-label="Hand placing a cube into a wall of sky blocks"></div>
      <p>Our strong team consists of group of consul-tant with vast experiences and outstanding achievement in years of services throughout the world. We've servicing the world's leading mobile network operators,</p>
      <span class="btn">Read More</span>
    </article>
    <article class="card">
      <div class="card-head">
        <span class="icon-circle"><svg width="14" height="14" viewBox="0 0 14 14"><rect x="1" y="2" width="12" height="11" rx="1" fill="#fff"/><path d="M3 6h2M6 6h2M9 6h2M3 8.5h2M6 8.5h2M9 8.5h2M3 11h2M6 11h2" stroke="#2e86bb" stroke-width="1.4"/></svg></span>
        <h2 class="section-title">Our Values</h2>
      </div>
      <div class="card-media media-values" role="img" aria-label="Diagram of company values: excellence, passion, integrity, teamwork, giving"></div>
      <p>The company outstanding values benefit from our in depth understanding of the mobile network challenge and requirement of today network environment scenario.</p>
      <span class="btn">Read More</span>
    </article>
  </section>

  <footer class="site-footer">COPYRIGHT © 2014 VELMORQUISTLINE SDN BHD. ALL RIGHTS RESERVED.</footer>
</body>
</html>
```